****Modern, Urban & Professional Business card for electrical company (electrician

Require a business card for an electrical company providing electrician services. Specifically residential and commercial property.

Business card must represent the company and brand and use the company colours in some way whether that be just the logo & name or full colour. Would like icons to be used for social media platforms email and telephone. Open to use of QR code but don’t want the card to look too busy.
QR Code must link to contact details on phone. Add contact with Name, Company, Phone Number, Website on phone contact details.

If you are a designer working on this job we would appreciate if you could follow our social media channels in exchange for a follow back. As a small start up business every like/follow helps :)

Would like to make the business card into a magnet (single sided also) future project

Industry/Entity Type

Electrician

Contact Information for Business Card

Colours to include but not limited to
dark blue -142455
sky blue - 0094da

91 x 55 mm size

Information to include:

Tom Hadleigh
Director
0271596034

www.brightwaveelectrical.co.nz
info@brightwaveelectrical.co.nz
www.Facebook.com/brightwaveelectrical
www.instagram.com/brightwave.electrical

Might be good to add:
24 hour emergency service

Requirements
Must have
• Email address included on card

```html
<!DOCTYPE html>
<html lang="en">
<head>
<meta charset="utf-8">
<title>Brightwave Electrical – Business Card</title>
<link rel="stylesheet" href="https://fonts.googleapis.com/css2?family=Roboto:wght@400;500;700&display=swap">
<style>
  :root {
    --navy: #1b2150;
    --sky: #1f8fd3;
    --sky-bright: #2196d8;
    --ink: #1e2240;
    --paper: #ffffff;
    --backdrop: #e9e7e3;
    --social-blue: #3b5a99;
    --social-brown: #6b3f36;
  }
  * { margin: 0; padding: 0; box-sizing: border-box; }
  html, body { width: 900px; height: 1200px; overflow: hidden; }
  body {
    background: var(--backdrop);
    position: relative;
    font-family: "Roboto", Arial, sans-serif;
    color: var(--ink);
  }
  .card {
    position: absolute;
    left: 76px;
    width: 747px;
    height: 451px;
    overflow: hidden;
    box-shadow: 0 6px 16px rgba(0,0,0,.25);
  }

  /* Front */
  .card-front { top: 117px; background: var(--paper); }
  .brand-mark {
    position: absolute;
    left: 537px; top: 52px;
    width: 102px; height: 102px;
    border-radius: 50%;
    background: var(--navy);
  }
  .brand-name {
    position: absolute;
    right: 51px; top: 162px;
    text-align: right;
    font-family: "Roboto", Arial, sans-serif;
    font-weight: 700;
    color: var(--navy);
    line-height: 1;
  }
  .brand-name .line-1 { display: block; font-size: 35px; letter-spacing: -0.5px; }
  .brand-name .line-2 { display: block; font-size: 25px; letter-spacing: 7px; margin-top: 8px; margin-right: -7px; }

  .person { position: absolute; left: 53px; top: 262px; }
  .person-name {
    font-size: 30px; font-weight: 500; letter-spacing: -0.3px;
    color: var(--navy); line-height: 1;
  }
  .person-name .surname { color: var(--sky); }
  .person-role { font-size: 20px; letter-spacing: 1px; margin-top: 5px; color: var(--navy); line-height: 1.1; }
  .rule {
    position: absolute; left: 141px; top: 310px;
    width: 555px; height: 1px; background: var(--navy);
  }

  .contact-list {
    position: absolute;
    top: 330px;
    list-style: none;
    display: flex; flex-direction: column; gap: 8px;
  }
  .contact-list.primary { left: 52px; }
  .contact-list.social { right: 51px; }
  .contact {
    display: flex; align-items: center; gap: 8px;
    height: 24px;
    font-size: 19px; letter-spacing: 1.1px; color: var(--ink);
    white-space: nowrap;
  }
  .contact svg { width: 22px; height: 22px; flex: none; }
  .social .contact { gap: 12px; }
  .social-dot { width: 22px; height: 22px; border-radius: 50%; flex: none; }
  .social-dot.facebook { background: var(--social-blue); }
  .social-dot.instagram { background: var(--social-brown); }

  .front-band {
    position: absolute; left: 0; bottom: 0;
    width: 100%; height: 17px; background: var(--navy);
  }

  /* Back */
  .card-back {
    top: 625px;
    background: linear-gradient(225deg, var(--sky-bright) 0%, #2586c6 30%, #2367a1 60%, #1d4677 100%);
  }
  .back-mark {
    position: absolute; left: 156px; top: 156px;
    width: 138px; height: 138px; border-radius: 50%;
    background: var(--navy);
  }
  .back-name {
    position: absolute; left: 304px; top: 180px;
    font-family: "Roboto", Arial, sans-serif;
    font-weight: 700; color: var(--paper); line-height: 1;
  }
  .back-name .line-1 { display: block; font-size: 46px; letter-spacing: -0.5px; }
  .back-name .line-2 { display: block; font-size: 34px; letter-spacing: 10px; margin-top: 10px; }
  .emergency-band {
    position: absolute; left: 0; top: 384px;
    width: 100%; height: 28px;
    background: linear-gradient(90deg, var(--navy) 0%, #2470ad 25%, var(--sky-bright) 50%, #2470ad 75%, var(--navy) 100%);
    color: var(--paper);
    font-size: 20px; font-weight: 500; letter-spacing: 1.2px;
    text-align: center; line-height: 28px;
  }
</style>
</head>
<body>
  <section class="card card-front" aria-label="Business card front">
    <div class="brand-mark" aria-hidden="true"></div>
    <h1 class="brand-name">
      <span class="line-1">BRIGHTWAVE</span>
      <span class="line-2">ELECTRICAL</span>
    </h1>

    <div class="person">
      <p class="person-name">TOM <span class="surname">HADLEIGH</span></p>
      <p class="person-role">Director</p>
    </div>
    <div class="rule"></div>

    <ul class="contact-list primary">
      <li class="contact contact-phone">
        <svg viewBox="0 0 22 22" aria-hidden="true">
          <circle cx="11" cy="11" r="11" fill="var(--sky)"/>
          <path d="M7.2 5.5c.6-.4 1.3-.3 1.7.3l1 1.6c.3.5.2 1.1-.2 1.5l-.7.6c.5 1.2 1.4 2.2 2.6 2.8l.6-.7c.4-.4 1-.5 1.5-.2l1.6 1c.6.4.7 1.1.3 1.7l-.6.8c-.6.7-1.6 1-2.5.6-3-1.2-5.3-3.6-6.4-6.6-.3-.9 0-1.9.7-2.5z" fill="#fff"/>
        </svg>
        0271596034
      </li>
      <li class="contact contact-web">
        <svg viewBox="0 0 22 22" aria-hidden="true">
          <circle cx="11" cy="11" r="11" fill="var(--sky)"/>
          <circle cx="11" cy="11" r="6.5" fill="none" stroke="#fff" stroke-width="1.4"/>
          <ellipse cx="11" cy="11" rx="2.8" ry="6.5" fill="none" stroke="#fff" stroke-width="1.2"/>
          <line x1="4.5" y1="11" x2="17.5" y2="11" stroke="#fff" stroke-width="1.2"/>
        </svg>
        www.brightwaveelectrical.co.nz
      </li>
      <li class="contact contact-email">
        <svg viewBox="0 0 22 22" aria-hidden="true">
          <circle cx="11" cy="11" r="11" fill="var(--sky)"/>
          <rect x="5" y="7" width="12" height="8.5" rx="1" fill="#fff"/>
          <path d="M5.5 7.6 11 12l5.5-4.4" fill="none" stroke="var(--sky)" stroke-width="1.3"/>
        </svg>
        info@brightwaveelectrical.co.nz
      </li>
    </ul>

    <ul class="contact-list social">
      <li class="contact contact-facebook"><span class="social-dot facebook" aria-hidden="true"></span>brightwaveelectrical</li>
      <li class="contact contact-instagram"><span class="social-dot instagram" aria-hidden="true"></span>brightwave.electrical</li>
    </ul>

    <div class="front-band"></div>
  </section>

  <section class="card card-back" aria-label="Business card back">
    <div class="back-mark" aria-hidden="true"></div>
    <h2 class="back-name">
      <span class="line-1">BRIGHTWAVE</span>
      <span class="line-2">ELECTRICAL</span>
    </h2>
    <p class="emergency-band">24 hour emergency service</p>
  </section>
</body>
</html>
```